Owner
Vireltex Golf Cart Cushion Covers
Bright & Fun-filled
Maelys Brant
348 Heron Mill Lane
Stamford, CT
maelysbrant@snugwraps.example
snugwraps.example
Snug Wraps are golf cart cushion covers made out of Vireltex Fleece. They are made in the USA.
Vireltex fleece golf cart cushion covers
available with custom embroidery

```html
<!DOCTYPE html>
<html lang="en">
<head>
<meta charset="utf-8">
<title>Snug Wraps — Business Card</title>
<link href="https://fonts.googleapis.com/css2?family=Open+Sans:wght@400;700&display=swap" rel="stylesheet">
<style>
  :root {
    --backdrop: #e6e6e8;
    --card-white: #ffffff;
    --card-black: #151515;
    --ink-dark: #2b2b2b;
    --ink-light: #ffffff;
    --ink-muted: #d8d8d8;
    --band-purple: #7b2f8f;
    --band-pink: #e0358a;
    --band-orange: #f28a1e;
    --band-green: #5bb544;
    --band-blue: #1f8ed6;
    --mark-dot: #e0358a;
  }
  * { margin: 0; padding: 0; box-sizing: border-box; }
  html, body {
    width: 1200px; height: 672px; overflow: hidden;
    background: var(--backdrop);
    font-family: "Open Sans", Arial, sans-serif;
  }
  .canvas { position: relative; width: 1200px; height: 672px; }
  .card {
    position: absolute; top: 191px;
    width: 500px; height: 290px;
    border-radius: 12px; overflow: hidden;
    background: var(--card-white);
    box-shadow: 0 6px 18px rgba(0,0,0,.18);
  }
  .card--front { left: 70px; }
  .card--back { left: 630px; }
  .card-swoosh { position: absolute; inset: 0; width: 100%; height: 100%; }
  .brand {
    position: absolute; display: flex; align-items: center; gap: 8px;
    color: var(--ink-dark); font-weight: 700; white-space: nowrap;
  }
  .brand-dot { border-radius: 50%; background: var(--mark-dot); flex: none; }
  .card--front .brand { left: 26px; top: 76px; font-size: 22px; }
  .card--front .brand-dot { width: 16px; height: 16px; }
  .card--back .brand { right: 32px; top: 118px; font-size: 34px; }
  .card--back .brand-dot { width: 24px; height: 24px; }
  .holder {
    position: absolute; left: 272px; top: 88px;
    color: var(--ink-light);
  }
  .holder-name { font-size: 21px; font-weight: 700; }
  .contact {
    position: absolute; left: 272px; top: 196px;
    font-size: 10.5px; line-height: 15px; color: var(--ink-muted);
  }
  .contact-label { font-weight: 700; color: var(--ink-light); }
  .website {
    position: absolute; left: 60px; top: 136px;
    font-size: 12px; color: var(--ink-dark);
  }
</style>
</head>
<body>
<div class="canvas">
  <section class="card card--front">
    <svg class="card-swoosh" viewBox="0 0 500 290" aria-hidden="true">
      <path d="M250 0 C215 120 165 220 110 290 L500 290 L500 0 Z" fill="var(--card-black)"/>
      <path d="M222 0 C190 120 140 220 86 290" fill="none" stroke="var(--band-purple)" stroke-width="6"/>
      <path d="M229 0 C197 120 147 220 92 290" fill="none" stroke="var(--band-pink)" stroke-width="6"/>
      <path d="M236 0 C204 120 153 220 98 290" fill="none" stroke="var(--band-orange)" stroke-width="6"/>
      <path d="M243 0 C210 120 159 220 104 290" fill="none" stroke="var(--band-green)" stroke-width="6"/>
      <path d="M250 0 C216 120 165 220 110 290" fill="none" stroke="var(--band-blue)" stroke-width="5"/>
    </svg>
    <div class="brand"><span class="brand-dot"></span>Snug Wraps</div>
    <div class="holder"><p class="holder-name">Maelys Brant</p></div>
    <div class="contact">
      <p>348 Heron Mill Lane</p>
      <p>Stamford, CT 06900</p>
      <p><span class="contact-label">C :</span> 070-555-0147</p>
      <p><span class="contact-label">E :</span> maelysbrant@snugwraps.example</p>
      <p><span class="contact-label">W :</span> snugwraps.example</p>
    </div>
  </section>

  <section class="card card--back">
    <p class="website">www.snugwraps.example</p>
    <div class="brand"><span class="brand-dot"></span>Snug Wraps</div>
  </section>
</div>
</body>
</html>
```